Design a Sleek, Modern Insert Card for a Wellness-Inspired Clinical Kit

We are looking for a sleek, professional insert card design to include inside our KELVARO Trial Boost kits — curated wellness pouches that will be sent to clinical research coordinators, physicians, and nurses participating in our KELVARO clinical study.
This insert should visually reflect the MORANTH Biologics and KELVARO brands (logos attached) — clean, modern, and cohesive — and serve as a small note of appreciation for their work.
Insert Text (exact wording to include):
Everything inside was chosen to fuel your focus, KELVARO your energy, and support your work advancing disc restoration.
Design Requirements:
Size: Small insert card that fits neatly inside a zippered pouch (approx. 4” x 6” or similar).
Orientation: Landscape
Logos:
KELVARO logo
MORANTH Biologics logo
(Both should be tastefully included and balanced within the design.)
Color Palette:
Shades of blue (from the KELVARO logo)
Shades of green (from the MORANTH logo)
Design Style:
Modern, clean, and minimalistic
Professional and medical, but still visually engaging
Premium feel (this will be part of an elegant, high-end kit)
Typography:
Easy to read, sans-serif fonts (open to designer’s creative judgment)
Should align with a clinical or wellness aesthetic (not overly corporate or decorative)
Examples of brand aesthetics that inspire us: Quince packaging, Hush app, Brimwell Nutrients, or ZERKA hydration branding
Target Market(s)
Physicians & nurses
Industry/Entity Type
Medical
Look and feel

```html
<!DOCTYPE html>
<html lang="en">
<head>
<meta charset="utf-8">
<title>KELVARO Trial Boost Insert Card</title>
<link rel="stylesheet" href="https://fonts.googleapis.com/css2?family=Abril+Fatface&family=Montserrat:wght@800&display=swap">
<style>
  :root {
    --blue: #42a9cb;
    --green: #6fc6a8;
    --white: #ffffff;
    --rule: #8a8a8a;
    --tint-green: #b6e0c6;
    --tint-teal: #8fd3d2;
    --tint-blue: #b3dbeb;
  }
  html, body {
    margin: 0;
    padding: 0;
    overflow: hidden;
    background: var(--white);
  }
  .card {
    position: relative;
    width: 1200px;
    height: 803px;
    overflow: hidden;
    background: var(--white);
  }
  .pattern-field {
    position: absolute;
    left: 12px;
    top: 12px;
    width: 1178px;
    height: 776px;
    background: linear-gradient(90deg, var(--tint-green) 0%, #c4e4d6 30%, var(--tint-teal) 60%, var(--tint-blue) 100%);
  }
  .bottom-rule {
    position: absolute;
    left: 0;
    top: 799px;
    width: 1200px;
    height: 1px;
    background: var(--rule);
  }
  .intro-banner {
    position: absolute;
    left: 100px;
    top: 199px;
    width: 702px;
    height: 100px;
    margin: 0;
    box-sizing: border-box;
    background: var(--blue);
    border: 2px solid var(--white);
    padding: 9px 40px 0 0;
    text-align: right;
    color: var(--white);
    font-family: "Montserrat", sans-serif;
    font-weight: 800;
    font-size: 34px;
    line-height: 39px;
    letter-spacing: 1px;
    white-space: nowrap;
  }
  .white-band {
    position: absolute;
    left: 300px;
    top: 499px;
    width: 900px;
    height: 101px;
    background: var(--white);
  }
  .brand-panel {
    position: absolute;
    left: 302px;
    top: 301px;
    width: 802px;
    height: 198px;
    box-sizing: border-box;
    background: var(--green);
    border: 2px solid var(--white);
    display: flex;
    align-items: center;
    justify-content: center;
  }
  .brand-word {
    font-family: "Abril Fatface", serif;
    color: var(--white);
    font-size: 150px;
    line-height: 1;
    letter-spacing: 2px;
    margin-top: 6px;
  }
  .closing-line {
    position: absolute;
    left: 345px;
    top: 509px;
    margin: 0;
    color: var(--blue);
    font-family: "Montserrat", sans-serif;
    font-weight: 800;
    font-size: 35px;
    line-height: 40px;
    letter-spacing: 1px;
    white-space: nowrap;
  }
</style>
</head>
<body>
  <main class="card">
    <div class="pattern-field" role="img" aria-label="Soft hexagon mosaic pattern fading from mint green to light blue"></div>
    <div class="white-band"></div>
    <p class="intro-banner">EVERYTHING INSIDE WAS<br>CHOSEN TO FUEL YOUR FOCUS</p>
    <div class="brand-panel">
      <span class="brand-word">KELVARO</span>
    </div>
    <p class="closing-line">YOUR ENERGY, AND SUPPORT YOUR<br>WORK ADVANCING DISC RESTORATION.</p>
    <div class="bottom-rule"></div>
  </main>
</body>
</html>
```